Bar Crawl Website required

Hi,

I need a new website (www.gladtonightwalk.com) to have the company information on one page (2 maximum) with an auto responder.
I will need to be shown how to update the site and use of auto responder. And I’m looking to build the site further as the crawls grow.
Ideally to be worked on with SEO – looking on Google for these words:

Best bars in London
Pub crawl London
Night out London
Bars London

I want the writing to be clear, concise and easily read in UK English but I need the design to be fun and cool (as its promoting a bar crawl).
We’re looking to drive people to the site and then attend a night. We’re targeting 18-35 year olds who live in London and want to party.
I want the picture gallery to look cool, the benefits clear to see and easy for the customer to sign up (website takes e-mail address)
We run bar crawls and our service is free to the customer, which we want to be prevalent but I want it to look like a trustworthy site and not one that is just trying to "sell" ie "whats the catch"?. Really want the website to be fun too and not over a background image.
I have provided the content (attached) but looking for you to come up with a design that is engaging, fun but also clear to read.

Examples:
http://www.morvalinnhop.com/
http://www.7loudeveningtrip.com/index.php?option=com_content&view=article&id=1&Itemid=1
http://www.hullabalootrek.com/

Thanks,
Updates

Hi,

The name of the company is called "Glad Tonight Walk".
Please can the benefits (free entry, free shot etc)  as per my word document be included on the homepage.
Can the content/structure be more similar to my word document that I uploaded.

Thanks,

Kit

Target Market(s)

18-35 year olds in London who like a night out.

Industry/Entity Type

It Company

Requirements
Must have
• Cool Photo Gallery
Autoresponder
Calendar with dates of crawls (I need to be able to update this)
Ideally on one page but will look at 2 pages if 1 page is not enough.
Should not have
• No Cheap looking background

```html
<!DOCTYPE html>
<html lang="en-GB">
<head>
<meta charset="utf-8">
<title>Glad Tonight Walk</title>
<link rel="stylesheet" href="https://fonts.googleapis.com/css2?family=Yanone+Kaffeesatz:wght@400;500;700&family=PT+Sans:wght@400;700&display=swap">
<style>
:root{
  --page:#150d13;
  --page-glow:#2a1424;
  --panel:#0b0a0b;
  --panel-edge:#3b3a3b;
  --title-band:#2b2a2b;
  --pink:#e8168f;
  --pink-soft:#ff4fb0;
  --lime:#9ccf12;
  --white:#ffffff;
  --text:#d8d8d8;
  --muted:#9a9a9a;
}
*{box-sizing:border-box;margin:0;padding:0}
html,body{width:1200px;height:1034px;overflow:hidden}
body{
  position:relative;
  background:radial-gradient(ellipse at 50% 0%,var(--page-glow),var(--page) 70%);
  font-family:"PT Sans",Arial,sans-serif;
  color:var(--text);
}
.brand{
  position:absolute;left:18px;top:48px;
  font-family:"Yanone Kaffeesatz",sans-serif;font-weight:500;font-size:40px;
  color:var(--pink-soft);
}
.tagline{position:absolute;left:250px;top:44px;font-size:14px;color:var(--muted)}
.home-icon{position:absolute;left:318px;top:14px}
.main-nav{position:absolute;left:440px;top:0;display:flex;gap:32px}
.main-nav a{
  font-family:"Yanone Kaffeesatz",sans-serif;font-size:28px;font-weight:500;
  color:var(--white);text-decoration:none;letter-spacing:.5px;
  padding:0 4px 4px 24px;border-bottom:2px solid #4a3a45;position:relative;line-height:30px;
}
.main-nav a::before{
  content:"";position:absolute;left:4px;top:11px;width:10px;height:10px;
  border-top:2px solid var(--white);border-right:2px solid var(--white);transform:rotate(45deg);
}
.search{position:absolute;left:816px;top:61px;display:flex;gap:7px}
.search input{width:253px;height:23px;border:0;background:#f4f4f0}
.search button{width:72px;height:23px;border:0;background:var(--pink);color:var(--white);font:700 17px "PT Sans",sans-serif}
.hero{
  position:absolute;left:47px;top:105px;width:1104px;height:376px;border-radius:22px;overflow:hidden;
  border:2px solid #5a5a3a;
  background:linear-gradient(100deg,#3d4a08 0%,#7d9a14 30%,#b4c82a 52%,#6b2a5a 78%,#c0247e 100%);
}
.hero-line1{position:absolute;left:326px;top:168px;font-family:"Yanone Kaffeesatz",sans-serif;font-size:30px;line-height:30px;color:var(--white)}
.hero-line2{position:absolute;left:248px;top:240px;font-family:"Yanone Kaffeesatz",sans-serif;font-size:44px;line-height:40px;color:var(--white)}
.panel{position:absolute;background:var(--panel);border:2px solid var(--panel-edge);border-radius:16px}
.panel-title{
  position:absolute;left:20px;top:16px;display:flex;align-items:center;gap:16px;
  font-family:"Yanone Kaffeesatz",sans-serif;font-size:36px;color:var(--white);line-height:40px;
}
.panel-title::before{
  content:"";width:24px;height:24px;background:var(--pink);border-radius:3px;
  clip-path:polygon(0 0,100% 0,100% 100%,0 100%);
  box-shadow:inset 0 0 0 0 transparent;
}
.title-band{position:absolute;top:24px;height:26px;background:var(--title-band);border-radius:2px}
.photo{position:absolute;border:2px solid #2c2c2c}
.lead{color:var(--lime);font-weight:700;font-size:17px}
.body-text{font-size:16px;line-height:23px;color:var(--text)}
.body-text a{color:var(--pink-soft)}
.more{position:absolute;font-weight:700;font-size:17px;color:var(--lime);text-decoration:underline}
.more::before{content:"";display:inline-block;width:8px;height:8px;border-radius:50%;background:var(--lime);margin-right:8px;vertical-align:middle}
.event{position:absolute;left:30px;width:280px}
.event-date{font-weight:700;font-size:17px;color:var(--white);padding-bottom:6px;border-bottom:2px solid var(--pink)}
.event-link{display:block;margin-top:8px;font-size:16px;color:var(--pink-soft)}
.subscribe-label{position:absolute;left:840px;top:952px;font-weight:700;font-size:17px;color:#cfcfcf}
.subscribe{position:absolute;left:840px;top:987px;display:flex;gap:10px}
.subscribe input{width:252px;height:28px;border:0;background:#f4f4f0;padding-left:12px;font:15px "PT Sans",sans-serif;color:#555}
.subscribe button{width:33px;height:28px;border:0;background:var(--pink);color:var(--white);font:700 16px "PT Sans",sans-serif}
</style>
</head>
<body>

<div class="brand">Glad Tonight Walk</div>
<p class="tagline">Your description goes here</p>
<svg class="home-icon" width="20" height="18" viewBox="0 0 20 18" aria-hidden="true">
  <path d="M2 9 L10 2 L18 9 M5 7 V16 H15 V7" fill="none" stroke="#ffffff" stroke-width="2"/>
</svg>

<nav class="main-nav">
  <a href="#">ABOUT US</a>
  <a href="#">TICKETS INFO</a>
  <a href="#">CONCERTS</a>
  <a href="#">GALLERY</a>
  <a href="#">CONTESTS</a>
</nav>

<form class="search"><input type="text" aria-label="Search"><button type="button">Search</button></form>

<section class="hero" role="img" aria-label="Silhouettes of people dancing at a club under green and pink lights">
  <p class="hero-line1">THE BIGGEST PARTIES<br>AT THE BIGGEST CLUB</p>
  <p class="hero-line2">SATURDAY<br>&nbsp;&nbsp;&nbsp;&nbsp;&nbsp;IS ALWAYS HERE !</p>
</section>

<section class="panel" style="left:47px;top:516px;width:743px;height:222px">
  <h2 class="panel-title">Welcome to the club!</h2>
  <div class="title-band" style="left:412px;width:172px"></div>
  <div style="position:absolute;left:36px;top:82px;width:536px">
    <p class="lead">Lorem ipsum dolor sit amet, consectetuer</p>
    <p class="body-text">adipiscing elit, sed diam nonummy nibh euismod tincidunt ut laoreet dolore magna aliquam erat volutpat. <a href="#">Ut wisi enim ad minim veniam</a> quis nostrud exerci tation ullamcorper suscipit lobortis nisl ut aliquip ex ea commodo consequat.</p>
  </div>
  <div class="photo" role="img" aria-label="Crowd on a club dance floor under purple lights" style="left:544px;top:63px;width:176px;height:146px;background:linear-gradient(160deg,#2a1b6a,#8a2a9a 55%,#d04aa0)"></div>
</section>

<section class="panel" style="left:47px;top:778px;width:356px;height:244px">
  <h2 class="panel-title">Dj party</h2>
  <div class="title-band" style="left:164px;width:170px"></div>
  <div class="photo" role="img" aria-label="DJ playing at the decks" style="left:-9px;top:75px;width:171px;height:153px;background:linear-gradient(150deg,#3a1830,#b02060 50%,#1aa0b0)"></div>
  <div style="position:absolute;left:176px;top:82px;width:160px">
    <p class="lead">Lorem ipsum</p>
    <p class="body-text">elit, sed diam nonummy nibh euismod tincidunt ut laoreet dolore.</p>
  </div>
  <a class="more" href="#" style="left:216px;top:208px">read more</a>
</section>

<section class="panel" style="left:431px;top:778px;width:359px;height:244px">
  <h2 class="panel-title">Gallery</h2>
  <div class="title-band" style="left:162px;width:174px"></div>
  <div class="photo" role="img" aria-label="Bar interior lit in red" style="left:12px;top:75px;width:138px;height:150px;background:linear-gradient(170deg,#3a0d10,#c0303a 50%,#2a0a0c)"></div>
  <div style="position:absolute;left:164px;top:82px;width:176px">
    <p class="lead">Lorem ipsum</p>
    <p class="body-text">adipiscing elit, sed diam nonummy nibh euismod tincidunt ut laoreet dolore.</p>
  </div>
  <a class="more" href="#" style="left:212px;top:208px">read more</a>
</section>

<section class="panel" style="left:816px;top:516px;width:335px;height:417px">
  <h2 class="panel-title">Latest events</h2>
  <div class="title-band" style="left:226px;width:86px"></div>
  <div class="event" style="top:78px">
    <p class="event-date">22/06/2006</p>
    <a class="event-link" href="#">Lorem ipsum dolor sit</a>
    <p class="body-text">adipiscing elit, sed diam nonummy nibh euismod tincidunt ut laoreet dolore magna.</p>
  </div>
  <div class="event" style="top:252px">
    <p class="event-date">22/06/2006</p>
    <a class="event-link" href="#">Lorem ipsum dolor sit</a>
    <p class="body-text">adipiscing elit, sed diam nonummy nibh euismod tincidunt ut laoreet dolore magna.</p>
  </div>
</section>

<p class="subscribe-label">Subscribe news &amp; events:</p>
<form class="subscribe"><input type="email" value="enter your e-mail" aria-label="E-mail address"><button type="button">ok</button></form>

</body>
</html>
```